BOLD & MINIMALIST DESIGN NEEDED

We want a very bold but minimalistic business card design that is impactful and utilizes both sides of the business card. Our current logo is included for your use.

We want bold fonts and good use of negative space. We don't want the logo to overpower the design.

Target Market(s)

Professionals who are building new commercial buildings.

Industry/Entity Type

Construction

Contact Information for Business Card

Name, Title, email, office phone, cell phone, website

Font styles to use
Serif
Sans Serif

Requirements
Must have
• Bold design!

```html
<!DOCTYPE html>
<html lang="en">
<head>
<meta charset="utf-8">
<title>Summitline Design + Build — Business Card</title>
<link rel="stylesheet" href="https://fonts.googleapis.com/css2?family=Montserrat:wght@800&family=Questrial&display=swap">
<style>
  :root {
    --backdrop: #2d2d2d;
    --card: #000000;
    --white: #f4f3f1;
    --green: #86c232;
    --green-light: #d4ecb8;
  }
  * { margin: 0; padding: 0; box-sizing: border-box; }
  html, body { width: 1200px; height: 1015px; overflow: hidden; }
  body {
    background: var(--backdrop);
    position: relative;
    font-family: "Questrial", sans-serif;
    color: var(--white);
  }
  .card {
    position: absolute;
    left: 250px;
    width: 700px;
    height: 400px;
    background: var(--card);
    border-bottom: 3px solid var(--green);
    border-left: 3px solid var(--green);
    overflow: hidden;
    box-shadow: 0 18px 30px rgba(0,0,0,0.45);
  }
  .card--front { top: 70px; }
  .card--back { top: 540px; }

  /* Front */
  .brand {
    position: absolute;
    left: 0; right: 0; top: 150px;
    text-align: center;
  }
  .brand__name {
    font-family: "Montserrat", sans-serif;
    font-weight: 800;
    font-size: 64px;
    letter-spacing: 1px;
    color: var(--white);
    line-height: 1;
  }
  .brand__rule {
    width: 440px;
    height: 1px;
    background: var(--white);
    margin: 12px auto 8px;
  }
  .brand__tagline {
    font-size: 20px;
    letter-spacing: 10px;
    color: var(--white);
  }

  /* Back */
  .person {
    position: absolute;
    left: 50px;
    top: 52px;
  }
  .person__name {
    font-family: "Montserrat", sans-serif;
    font-weight: 800;
    font-size: 30px;
    letter-spacing: 0.5px;
  }
  .person__rule {
    width: 300px;
    height: 1px;
    background: var(--green);
    margin: 6px 0 6px;
  }
  .person__title {
    font-size: 17px;
    color: var(--green);
    letter-spacing: 0.5px;
  }
  .contact {
    position: absolute;
    left: 50px;
    bottom: 34px;
    list-style: none;
  }
  .contact__item {
    display: flex;
    align-items: center;
    gap: 10px;
    font-size: 20px;
    line-height: 30px;
  }
  .contact__icon { width: 18px; height: 18px; flex: none; }
  .accent-block {
    position: absolute;
    right: -60px;
    bottom: -60px;
    width: 300px;
    height: 340px;
    background: linear-gradient(200deg, var(--green-light) 0%, var(--green) 70%);
  }
</style>
</head>
<body>

<section class="card card--front" aria-label="Card front">
  <div class="brand">
    <div class="brand__name">SUMMITLINE</div>
    <div class="brand__rule"></div>
    <div class="brand__tagline">DESIGN + BUILD</div>
  </div>
</section>

<section class="card card--back" aria-label="Card back">
  <div class="person">
    <div class="person__name">DANIEL CARVER</div>
    <div class="person__rule"></div>
    <div class="person__title">MANAGING DIRECTOR</div>
  </div>

  <ul class="contact">
    <li class="contact__item">
      <svg class="contact__icon" viewBox="0 0 24 24" fill="var(--green)"><path d="M6.6 10.8a15 15 0 0 0 6.6 6.6l2.2-2.2a1 1 0 0 1 1-.25 11.4 11.4 0 0 0 3.6.57 1 1 0 0 1 1 1V20a1 1 0 0 1-1 1A17 17 0 0 1 3 4a1 1 0 0 1 1-1h3.5a1 1 0 0 1 1 1c0 1.25.2 2.45.57 3.6a1 1 0 0 1-.25 1z"/></svg>
      041-550 218 364
    </li>
    <li class="contact__item">
      <svg class="contact__icon" viewBox="0 0 24 24" fill="none" stroke="var(--green)" stroke-width="2"><rect x="6" y="2" width="12" height="20" rx="2"/><line x1="10" y1="18" x2="14" y2="18"/></svg>
      041-550 218 365
    </li>
    <li class="contact__item">
      <svg class="contact__icon" viewBox="0 0 24 24" fill="none" stroke="var(--green)" stroke-width="2"><rect x="2" y="5" width="20" height="14"/><path d="M2 5l10 8 10-8"/></svg>
      info@summitline.co
    </li>
    <li class="contact__item">
      <svg class="contact__icon" viewBox="0 0 24 24" fill="none" stroke="var(--green)" stroke-width="2"><circle cx="12" cy="12" r="10"/><ellipse cx="12" cy="12" rx="4" ry="10"/><line x1="2" y1="12" x2="22" y2="12"/></svg>
      www.summitline.co
    </li>
  </ul>

  <div class="accent-block"></div>
</section>

</body>
</html>
```